Range of Mayonise Bottles

We are wanting a Logo and Artwork for a Range of Mayonnaise’s.
There are 3 lines in total
Mayonnaise Regular
Mayonnaise and Garlic
Aioli ( Mayo and Lemon)
All 300g Upside down Style Bottle.
Image attached.
Logo: is Brindle Pantry

Target Market(s)

Supermarket Line

Requirements
Must have
• Brindle Pantry must be on all 3 lines
Pictures on Front
weight on Front
Ingredinets Only English
we will provide Nutrtioanl Info so please leave space
Barcodes I will upload
Nice to have
• Image of Mayonaise

```html
<!DOCTYPE html>
<html lang="en">
<head>
<meta charset="utf-8">
<title>Brindle Pantry Mayonnaise Range – Labels</title>
<link rel="stylesheet" href="https://fonts.googleapis.com/css2?family=Allura&family=Barlow:wght@600;800&family=Teko:wght@400;500&display=swap">
<style>
  :root{
    --backdrop-top:#5db6e2;
    --backdrop-bottom:#2a93cf;
    --cream-light:#fdfaf0;
    --cream-mid:#f3e7c8;
    --cream-deep:#e6d19f;
    --photo-warm:#ecd9b4;
    --rule-white:#f4f4f2;
    --brand-red:#d9232a;
    --script-ink:#1d2040;
    --garlic:#3c9a30;
    --garlic-light:#7cc242;
    --regular:#0f3f70;
    --regular-light:#1d6aa6;
    --lemon:#ec7014;
    --lemon-light:#f5a41f;
    --white:#ffffff;
  }
  *{margin:0;padding:0;box-sizing:border-box}
  html,body{width:1200px;height:944px;overflow:hidden}
  body{
    background:radial-gradient(ellipse at 50% 35%,var(--backdrop-top),var(--backdrop-bottom));
    font-family:"Barlow",sans-serif;
  }
  .range{position:relative;width:1200px;height:944px}
  .label{position:absolute;top:150px;width:340px;height:640px}
  .label--garlic{left:60px;--accent:var(--garlic);--accent-light:var(--garlic-light)}
  .label--regular{left:430px;top:130px;--accent:var(--regular);--accent-light:var(--regular-light)}
  .label--lemon{left:800px;--accent:var(--lemon);--accent-light:var(--lemon-light)}
  .label-shape{position:absolute;inset:0;width:340px;height:640px}
  .brand{
    position:absolute;top:92px;left:0;width:100%;
    text-align:center;color:var(--brand-red);
    font-family:"Barlow",sans-serif;font-weight:800;
    font-size:30px;line-height:0.95;letter-spacing:0.5px;text-transform:uppercase;
  }
  .product-name{
    position:absolute;top:168px;left:0;width:100%;
    text-align:center;color:var(--accent);
    font-family:"Teko",sans-serif;font-weight:500;
    font-size:70px;line-height:1;letter-spacing:1px;
  }
  .variant{
    position:absolute;top:222px;left:40px;width:100%;
    text-align:center;color:var(--script-ink);
    font-family:"Allura",cursive;font-size:44px;line-height:1;
  }
  .food-image{
    position:absolute;top:280px;left:62px;width:216px;height:250px;
    border-radius:46% 46% 42% 42%;
    background:radial-gradient(ellipse at 50% 45%,var(--cream-light),var(--photo-warm));
  }
  .weight{
    position:absolute;top:592px;left:0;width:100%;
    text-align:center;color:var(--white);
    font-family:"Barlow",sans-serif;font-weight:600;font-size:20px;
  }
</style>
</head>
<body>
<main class="range">

  <section class="label label--garlic">
    <svg class="label-shape" viewBox="0 0 340 640" aria-hidden="true">
      <defs>
        <radialGradient id="cream-garlic" cx="50%" cy="50%" r="60%">
          <stop offset="0" stop-color="#fdfaf0"/><stop offset="0.6" stop-color="#f3e7c8"/><stop offset="1" stop-color="#e6d19f"/>
        </radialGradient>
        <linearGradient id="band-garlic" x1="0" x2="1"><stop offset="0" stop-color="#3c9a30"/><stop offset="1" stop-color="#7cc242"/></linearGradient>
        <clipPath id="clip-garlic"><path d="M10,80 Q170,0 330,80 C345,250 310,330 325,560 Q170,660 15,560 C30,330 -5,250 10,80 Z"/></clipPath>
      </defs>
      <g clip-path="url(#clip-garlic)">
        <rect width="340" height="640" fill="url(#cream-garlic)"/>
        <path d="M0,0 H340 V66 Q170,40 0,160 Z" fill="url(#band-garlic)"/>
        <path d="M0,160 Q170,40 340,66" fill="none" stroke="#f4f4f2" stroke-width="8"/>
        <path d="M0,560 Q190,560 340,470 V640 H0 Z" fill="url(#band-garlic)"/>
        <path d="M0,560 Q190,560 340,470" fill="none" stroke="#f4f4f2" stroke-width="8"/>
      </g>
    </svg>
    <p class="brand">Brindle<br>Pantry</p>
    <h2 class="product-name">MAYONNAISE</h2>
    <p class="variant">Garlic</p>
    <div class="food-image" role="img" aria-label="Photo of a bowl of mayonnaise with garlic cloves, red onion slices, chilli and a cracked egg"></div>
    <p class="weight">300 G</p>
  </section>

  <section class="label label--regular">
    <svg class="label-shape" viewBox="0 0 340 640" aria-hidden="true">
      <defs>
        <radialGradient id="cream-regular" cx="50%" cy="50%" r="60%">
          <stop offset="0" stop-color="#fdfaf0"/><stop offset="0.6" stop-color="#f3e7c8"/><stop offset="1" stop-color="#e6d19f"/>
        </radialGradient>
        <linearGradient id="band-regular" x1="0" x2="1"><stop offset="0" stop-color="#0f3f70"/><stop offset="1" stop-color="#1d6aa6"/></linearGradient>
        <clipPath id="clip-regular"><path d="M10,80 Q170,0 330,80 C345,250 310,330 325,560 Q170,660 15,560 C30,330 -5,250 10,80 Z"/></clipPath>
      </defs>
      <g clip-path="url(#clip-regular)">
        <rect width="340" height="640" fill="url(#cream-regular)"/>
        <path d="M0,0 H340 V66 Q170,40 0,160 Z" fill="url(#band-regular)"/>
        <path d="M0,160 Q170,40 340,66" fill="none" stroke="#f4f4f2" stroke-width="8"/>
        <path d="M0,560 Q190,560 340,470 V640 H0 Z" fill="url(#band-regular)"/>
        <path d="M0,560 Q190,560 340,470" fill="none" stroke="#f4f4f2" stroke-width="8"/>
      </g>
    </svg>
    <p class="brand">Brindle<br>Pantry</p>
    <h2 class="product-name">MAYONNAISE</h2>
    <p class="variant">Regular</p>
    <div class="food-image" role="img" aria-label="Photo of a bowl of mayonnaise with red onion slices, chilli, herbs and a cracked egg"></div>
    <p class="weight">300 G</p>
  </section>

  <section class="label label--lemon">
    <svg class="label-shape" viewBox="0 0 340 640" aria-hidden="true">
      <defs>
        <radialGradient id="cream-lemon" cx="50%" cy="50%" r="60%">
          <stop offset="0" stop-color="#fdfaf0"/><stop offset="0.6" stop-color="#f3e7c8"/><stop offset="1" stop-color="#e6d19f"/>
        </radialGradient>
        <linearGradient id="band-lemon" x1="0" x2="1"><stop offset="0" stop-color="#ec7014"/><stop offset="1" stop-color="#f5a41f"/></linearGradient>
        <clipPath id="clip-lemon"><path d="M10,80 Q170,0 330,80 C345,250 310,330 325,560 Q170,660 15,560 C30,330 -5,250 10,80 Z"/></clipPath>
      </defs>
      <g clip-path="url(#clip-lemon)">
        <rect width="340" height="640" fill="url(#cream-lemon)"/>
        <path d="M0,0 H340 V66 Q170,40 0,160 Z" fill="url(#band-lemon)"/>
        <path d="M0,160 Q170,40 340,66" fill="none" stroke="#f4f4f2" stroke-width="8"/>
        <path d="M0,560 Q190,560 340,470 V640 H0 Z" fill="url(#band-lemon)"/>
        <path d="M0,560 Q190,560 340,470" fill="none" stroke="#f4f4f2" stroke-width="8"/>
      </g>
    </svg>
    <p class="brand">Brindle<br>Pantry</p>
    <h2 class="product-name">MAYONNAISE</h2>
    <p class="variant">Lemon</p>
    <div class="food-image" role="img" aria-label="Photo of a bowl of mayonnaise with lemon slices, red onion, chilli and a cracked egg"></div>
    <p class="weight">300 G</p>
  </section>

</main>
</body>
</html>
```